Restaurant service company needs a website!

I am looking for a skilled web designer/developer to create a professional, responsive, and easy-to-navigate website for my company, which specializes in servicing restaurant cooking equipment. The site should communicate trust, reliability, and technical expertise to our target audience, restaurant owners, managers, and commercial kitchen operators. I have included the company logos, if any other format for them is needed please let me know.

Target Market(s)

restaurant owners, managers, and commercial kitchen operators

Industry/Entity Type

Commercial Kitchen Equipment Service

Coding

Coded - Design and coding required

Number of Pages Required

1 page

Font styles to use
Serif
Sans Serif

Requirements
Must have
• Contact and service request forms, Click-to-call functionality for mobile, Clean, modern layout with strong visuals, Easy navigation, mobile-friendly
Nice to have
• Testimonials or Reviews, If possible a click-to-text functionality for mobile.
Should not have
• Any mention of Refrigeration or HVAC, "Free Quotes"

```html
<!DOCTYPE html>
<html lang="en">
<head>
<meta charset="utf-8">
<title>Meridian Restaurant Service</title>
<link href="https://fonts.googleapis.com/css2?family=Montserrat:wght@400;500;600;700;800&display=swap" rel="stylesheet">
<style>
:root{
  --teal:#1d6c84;
  --teal-dark:#15566b;
  --teal-deep:#0f4456;
  --orange:#f0960f;
  --ink:#222a2e;
  --text:#3a4246;
  --muted:#5d6468;
  --silver-1:#e9ecee;
  --silver-2:#cfd5d9;
  --charcoal:#26292b;
  --white:#ffffff;
}
*{box-sizing:border-box;margin:0;padding:0}
html,body{width:1200px;height:4769px;overflow:hidden;background:var(--white)}
body{font-family:"Montserrat",Arial,sans-serif;color:var(--text)}
.page{position:relative;width:1200px;height:4769px;overflow:hidden}
.abs{position:absolute}
.btn{position:absolute;display:flex;align-items:center;justify-content:center;gap:8px;border-radius:30px;color:var(--white);font-weight:700;font-size:13px;letter-spacing:.3px;text-transform:uppercase}
.btn-teal{background:var(--teal-dark)}
.btn-orange{background:var(--orange)}
.heading{font-weight:700;color:var(--teal);text-transform:uppercase;letter-spacing:.5px}
.eyebrow{font-size:15px;letter-spacing:1px;text-transform:uppercase;color:var(--ink)}
.rule{position:absolute;height:3px;background:var(--teal)}
/* header */
.site-header{left:0;top:0;width:1200px;height:76px;background:var(--white);box-shadow:0 1px 4px rgba(0,0,0,.08);z-index:5}
.brand{position:absolute;left:108px;top:14px;display:flex;align-items:center;gap:10px}
.brand-mark{width:16px;height:16px;border:3px solid var(--teal)}
.brand-name{font-weight:800;font-size:24px;color:var(--teal);letter-spacing:.5px;line-height:1}
.brand-sub{font-weight:700;font-size:9px;color:var(--teal);letter-spacing:2px;margin-top:3px}
.nav a{position:absolute;top:31px;font-size:12px;font-weight:700;color:var(--teal-dark);text-decoration:none}
.nav .active-bar{position:absolute;left:381px;top:74px;width:75px;height:3px;background:var(--teal)}
.header-phone{position:absolute;left:928px;top:24px;display:flex;align-items:center;gap:7px;font-size:14px;font-weight:600;color:var(--ink)}
.icon-circle{display:flex;align-items:center;justify-content:center;border-radius:50%;background:var(--teal-dark)}
/* hero */
.hero{left:0;top:76px;width:1200px;height:674px;background:linear-gradient(90deg,#b9a99a 0%,#e4e6e8 30%,#eef0f1 55%,#c4c9cc 80%,#9ea4a8 100%)}
.hero-glow{left:300px;top:76px;width:600px;height:674px;background:radial-gradient(ellipse at center,rgba(255,255,255,.9),rgba(255,255,255,0) 70%)}
.hero-eyebrow{left:0;top:210px;width:1200px;text-align:center;font-size:15px;letter-spacing:3px;color:var(--ink);font-weight:500}
.hero-eyebrow span{display:inline-block;width:38px;height:1px;background:var(--ink);vertical-align:middle;margin:0 10px}
.hero-title{left:0;top:244px;width:1200px;text-align:center;font-size:42px;font-weight:700;line-height:46px;color:var(--teal);letter-spacing:1px}
.hero-title .dark{color:var(--ink)}
/* about */
.about-text{left:656px;width:470px;font-size:17.5px;line-height:27px;color:var(--text)}
.about-quote{left:656px;top:1080px;width:480px;border-left:2px solid var(--teal);padding-left:14px;font-size:17.5px;line-height:27px}
/* services */
.band-silver{background:linear-gradient(180deg,#e5e8ea 0%,#f4f5f6 40%,#d9dee1 100%)}
.svc-photo{top:1589px;width:317px;height:258px}
.svc-card{top:1793px;width:289px;height:213px;background:var(--white);box-shadow:0 4px 14px rgba(0,0,0,.1)}
.svc-card.featured{background:var(--teal)}
.svc-card h3{position:absolute;left:36px;top:48px;font-size:17px;line-height:24px;font-weight:600;color:var(--ink);text-transform:uppercase}
.svc-card.featured h3,.svc-card.featured p{color:var(--white)}
.svc-card p{position:absolute;left:36px;top:106px;width:230px;border-left:1.5px solid var(--muted);padding-left:12px;font-size:12.5px;line-height:19.5px;color:var(--text)}
.svc-card.featured p{border-color:var(--white)}
.svc-icon{position:absolute;left:36px;top:-35px;width:68px;height:68px;border-radius:50%;background:var(--teal);border:4px solid var(--white);display:flex;align-items:center;justify-content:center}
/* why */
.feature h4{font-size:13.5px;font-weight:700;color:var(--teal);text-transform:uppercase}
.feature p{font-size:11.5px;line-height:19px;color:var(--text);margin-top:4px}
.feature{position:absolute;width:230px}
.feature.left{text-align:right}
.feat-box{position:absolute;width:84px;height:82px;border:2px solid var(--silver-2);background:var(--white);display:flex;align-items:center;justify-content:center}
.feat-box div{width:68px;height:66px;background:var(--teal-dark);display:flex;align-items:center;justify-content:center}
/* reviews */
.review{position:absolute;background:var(--white);box-shadow:0 4px 18px rgba(0,0,0,.12);text-align:center;color:var(--text)}
.review p{font-size:15.5px;line-height:27px}
.review-side p{font-size:11px;line-height:20px}
/* contact */
.contact-left{left:0;top:3852px;width:602px;height:640px;background:linear-gradient(135deg,#33383b,#1c1e20)}
.contact-right{left:602px;top:3852px;width:598px;height:640px;background:linear-gradient(135deg,#2b7d95,#175f75)}
.contact-item{position:absolute;left:146px;display:flex;align-items:center;gap:14px;color:var(--white);font-size:17px;line-height:21px}
.contact-item .ic{width:40px;height:40px;border-radius:50%;background:var(--white);display:flex;align-items:center;justify-content:center;flex:none}
.field{position:absolute;background:var(--white);font-size:13px;color:var(--ink);padding:12px 0 0 24px}
/* footer */
.footer-nav a{position:absolute;top:4520px;font-size:14px;font-weight:700;color:var(--ink);text-decoration:none}
.footer-dot{position:absolute;top:4526px;width:5px;height:5px;border-radius:50%;background:var(--teal)}
.footer-contact{position:absolute;top:4626px;display:flex;align-items:center;gap:10px;font-size:14.5px;font-weight:500;color:var(--ink)}
.social{position:absolute;top:4707px;width:32px;height:32px;border-radius:50%;background:var(--teal)}
</style>
</head>
<body>
<div class="page">

  <!-- HEADER -->
  <header class="abs site-header">
    <div class="brand">
      <div class="brand-mark"></div>
      <div>
        <div class="brand-name">MERIDIAN</div>
        <div class="brand-sub">RESTAURANT SERVICE</div>
      </div>
    </div>
    <nav class="nav">
      <a style="left:381px">ABOUT US</a>
      <a style="left:496px">SERVICES</a>
      <a style="left:607px">WHY US</a>
      <a style="left:703px">REVIEWS</a>
      <a style="left:811px">CONTACT US</a>
      <div class="active-bar"></div>
    </nav>
    <div class="header-phone">
      <div class="icon-circle" style="width:30px;height:30px">
        <svg width="15" height="15" viewBox="0 0 24 24"><path fill="#fff" d="M6.6 10.8a15 15 0 0 0 6.6 6.6l2.2-2.2c.3-.3.7-.4 1-.2 1.1.4 2.3.6 3.6.6.6 0 1 .4 1 1V20c0 .6-.4 1-1 1A17 17 0 0 1 3 4c0-.6.4-1 1-1h3.5c.6 0 1 .4 1 1 0 1.3.2 2.5.6 3.6.1.3 0 .7-.2 1z"/></svg>
      </div>
      (+100) 555 0142
    </div>
  </header>

  <!-- HERO -->
  <section class="abs hero" role="img" aria-label="Technician servicing a stainless steel commercial kitchen with ovens and fryers"></section>
  <div class="abs hero-glow"></div>
  <div class="abs hero-eyebrow"><span></span>MERIDIAN RESTAURANT SERVICE<span></span></div>
  <h1 class="abs hero-title">RELIABLE COMMERCIAL<br>KITCHEN EQUIPMENT<br><span class="dark">SERVICING</span></h1>
  <div class="btn btn-teal" style="left:409px;top:415px;width:182px;height:41px">REQUEST SERVICE ›</div>
  <div class="btn btn-orange" style="left:598px;top:415px;width:182px;height:41px">
    <svg width="13" height="13" viewBox="0 0 24 24"><path fill="#fff" d="M6.6 10.8a15 15 0 0 0 6.6 6.6l2.2-2.2c.3-.3.7-.4 1-.2 1.1.4 2.3.6 3.6.6.6 0 1 .4 1 1V20c0 .6-.4 1-1 1A17 17 0 0 1 3 4c0-.6.4-1 1-1h3.5c.6 0 1 .4 1 1 0 1.3.2 2.5.6 3.6.1.3 0 .7-.2 1z"/></svg>
    CALL US NOW ›</div>
  <svg class="abs" style="left:0;top:620px" width="1200" height="131" viewBox="0 0 1200 131">
    <polygon points="0,131 0,125 600,8 1200,95 1200,131" fill="#fff"/>
    <polyline points="0,125 600,8 1200,95" fill="none" stroke="#c3c8cc" stroke-width="2"/>
  </svg>

  <!-- ABOUT -->
  <section>
    <div class="abs" role="img" aria-label="Bright commercial kitchen with steel appliances and white tiles" style="left:110px;top:800px;width:430px;height:420px;border-radius:14px;background:linear-gradient(135deg,#e6e8ea,#b5bcc1)"></div>
    <div class="abs" role="img" aria-label="Technician repairing a commercial cooktop" style="left:350px;top:1043px;width:250px;height:220px;border-radius:8px;border:5px solid var(--white);background:linear-gradient(135deg,#9fa6ab,#4b5a66)"></div>

    <h2 class="abs heading" style="left:656px;top:823px;font-size:32px;line-height:42px">ABOUT MERIDIAN<br>RESTAURANT SERVICE</h2>
    <div class="rule" style="left:656px;top:917px;width:118px;height:2px"></div>
    <p class="abs about-text" style="top:936px">Lorem ipsum dolor sit amet, consectetur adipiscing elit, sed do eiusmod tempor incididunt ut labore et dolore magna aliqua. Quis ipsum suspendisse ultrices gravida. Risus commodo viverra</p>
    <p class="abs about-quote">Lorem ipsum dolor sit amet, consectetur adipiscing elit, sed do eiusmod tempor incididunt ut labore et dolore magna aliqua ipsum suspendisse</p>
    <div class="btn btn-teal" style="left:654px;top:1188px;width:222px;height:52px;font-size:14px">REQUEST SERVICE ›</div>
  </section>

  <!-- SERVICES -->
  <section class="abs band-silver" style="left:0;top:1422px;width:1200px;height:680px"></section>
  <div class="abs" style="left:592px;top:1385px;width:2px;height:60px;background:var(--teal)"></div>
  <h2 class="abs heading" style="left:0;top:1502px;width:1200px;text-align:center;font-size:33px">SERVICES WE PROVIDE</h2>
  <div class="rule" style="left:558px;top:1555px;width:84px;height:2px"></div>

  <div class="abs svc-photo" role="img" aria-label="Gloved hands repairing a gas burner valve" style="left:102px;background:linear-gradient(135deg,#3d4347,#8b7f52)"></div>
  <div class="abs svc-photo" role="img" aria-label="Black gas range grates on a commercial stove" style="left:456px;background:linear-gradient(135deg,#2a2d30,#6d7276)"></div>
  <div class="abs svc-photo" role="img" aria-label="Technician inspecting a wall oven in a kitchen" style="left:796px;background:linear-gradient(135deg,#a78a6b,#5c5e62)"></div>

  <div class="abs svc-card" style="left:118px">
    <div class="svc-icon"><svg width="34" height="30" viewBox="0 0 34 30"><rect x="2" y="4" width="30" height="22" fill="none" stroke="#fff" stroke-width="2"/><line x1="2" y1="11" x2="32" y2="11" stroke="#fff" stroke-width="2"/></svg></div>
    <h3>Cooking<br>Equipment Repair</h3>
    <p>Lorem ipsum dolor sit amet, consectetur adipiscing elit, sed do eiusmod tempor incididunt ut labore et dolore magna</p>
  </div>
  <div class="abs svc-card featured" style="left:468px">
    <div class="svc-icon"><svg width="32" height="32" viewBox="0 0 32 32"><circle cx="16" cy="16" r="11" fill="none" stroke="#fff" stroke-width="2"/><circle cx="16" cy="16" r="4" fill="none" stroke="#fff" stroke-width="2"/></svg></div>
    <h3>Preventive<br>Maintenance</h3>
    <p>Lorem ipsum dolor sit amet, consectetur adipiscing elit, sed do eiusmod tempor incididunt ut labore et dolore magna</p>
  </div>
  <div class="abs svc-card" style="left:815px">
    <div class="svc-icon"><svg width="32" height="32" viewBox="0 0 32 32"><rect x="5" y="9" width="22" height="18" fill="none" stroke="#fff" stroke-width="2"/><line x1="16" y1="3" x2="16" y2="9" stroke="#fff" stroke-width="2"/></svg></div>
    <h3>Emergency<br>Servicing</h3>
    <p>Lorem ipsum dolor sit amet, consectetur adipiscing elit, sed do eiusmod tempor incididunt ut labore et dolore magna</p>
  </div>

  <!-- WHY CHOOSE US -->
  <div class="abs eyebrow" style="left:0;top:2148px;width:1200px;text-align:center;font-size:14px">WHY WE ARE</div>
  <h2 class="abs heading" style="left:0;top:2174px;width:1200px;text-align:center;font-size:33px">WHY CHOOSE US</h2>
  <div class="abs" style="left:89px;top:2427px;width:1022px;height:2px;background:#d3d8db"></div>
  <div class="abs" role="img" aria-label="Chef cooking over a gas burner flame" style="left:470px;top:2290px;width:250px;height:280px;border-radius:22px;background:linear-gradient(135deg,#c9b79e,#8a8f93)"></div>

  <div class="feature left" style="left:83px;top:2300px"><h4>Fast Response Times</h4><p>Lorem ipsum dolor sit amet, consectetur adipiscing elit, sed do eiusmod tempor incididunt ut labore et</p></div>
  <div class="feature left" style="left:83px;top:2478px"><h4>Certified Technicians</h4><p>Lorem ipsum dolor sit amet, consectetur adipiscing elit, sed do eiusmod tempor incididunt ut labore et</p></div>
  <div class="feature" style="left:874px;top:2294px"><h4>Reliable Service</h4><p>Lorem ipsum dolor sit amet, consectetur adipiscing elit, sed do eiusmod tempor incididunt ut labore et</p></div>
  <div class="feature" style="left:874px;top:2472px"><h4>Customer-First Approach</h4><p>Lorem ipsum dolor sit amet, consectetur adipiscing elit, sed do eiusmod tempor incididunt ut labore et</p></div>

  <div class="feat-box" style="left:335px;top:2291px"><div><svg width="34" height="34" viewBox="0 0 34 34"><circle cx="17" cy="17" r="13" fill="none" stroke="#fff" stroke-width="2"/><path d="M17 9v8l5 4" fill="none" stroke="#fff" stroke-width="2"/></svg></div></div>
  <div class="feat-box" style="left:335px;top:2470px"><div><svg width="34" height="34" viewBox="0 0 34 34"><circle cx="17" cy="12" r="6" fill="none" stroke="#fff" stroke-width="2"/><path d="M6 30c1-7 6-10 11-10s10 3 11 10" fill="none" stroke="#fff" stroke-width="2"/></svg></div></div>
  <div class="feat-box" style="left:767px;top:2291px"><div><svg width="34" height="34" viewBox="0 0 34 34"><circle cx="17" cy="17" r="12" fill="none" stroke="#fff" stroke-width="2"/><path d="M11 17l4 4 8-8" fill="none" stroke="#fff" stroke-width="2"/></svg></div></div>
  <div class="feat-box" style="left:767px;top:2470px"><div><svg width="34" height="34" viewBox="0 0 34 34"><rect x="5" y="12" width="24" height="16" fill="none" stroke="#fff" stroke-width="2"/><line x1="5" y1="19" x2="29" y2="19" stroke="#fff" stroke-width="2"/><path d="M13 12V8h8v4" fill="none" stroke="#fff" stroke-width="2"/></svg></div></div>

  <div class="btn btn-orange" style="left:372px;top:2663px;width:219px;height:52px;font-size:14px">REQUEST SERVICE ›</div>
  <div class="btn btn-teal" style="left:602px;top:2663px;width:217px;height:52px;font-size:14px;background:var(--teal)">
    <svg width="14" height="14" viewBox="0 0 24 24"><path fill="#fff" d="M6.6 10.8a15 15 0 0 0 6.6 6.6l2.2-2.2c.3-.3.7-.4 1-.2 1.1.4 2.3.6 3.6.6.6 0 1 .4 1 1V20c0 .6-.4 1-1 1A17 17 0 0 1 3 4c0-.6.4-1 1-1h3.5c.6 0 1 .4 1 1 0 1.3.2 2.5.6 3.6.1.3 0 .7-.2 1z"/></svg>
    CALL US NOW ›</div>

  <!-- CTA + REVIEWS BAND -->
  <section class="abs band-silver" style="left:0;top:2760px;width:1200px;height:1092px;background:linear-gradient(180deg,#f3f4f5 0%,#dfe3e6 50%,#eceef0 100%)"></section>
  <div class="abs" role="img" aria-label="Technician in safety glasses checking equipment with a laptop in a commercial kitchen" style="left:96px;top:2791px;width:1017px;height:469px;background:linear-gradient(90deg,#8c9296,#c8cdd0 60%,#6a7074)"></div>
  <svg class="abs" style="left:96px;top:2791px" width="620" height="469" viewBox="0 0 620 469">
    <polygon points="0,0 617,0 450,469 0,469" fill="#1d6c84"/>
  </svg>
  <h2 class="abs" style="left:181px;top:2896px;font-size:36px;line-height:41px;font-weight:700;color:var(--white)">COOKING EQUIPMENT<br>CAN'T WAIT. REQUEST<br>SERVICE NOW!</h2>
  <p class="abs" style="left:189px;top:3028px;width:400px;font-size:15px;line-height:25px;color:var(--white)">Lorem ipsum dolor sit amet, consectetur adipiscing elit, sed do eiusmod tempor</p>
  <div class="btn btn-orange" style="left:185px;top:3103px;width:211px;height:50px;font-size:14px">REQUEST SERVICE ›</div>

  <div class="abs eyebrow" style="left:0;top:3299px;width:1200px;text-align:center;font-size:14px">CUSTOMER REVIEWS</div>
  <h2 class="abs heading" style="left:0;top:3325px;width:1200px;text-align:center;font-size:33px">WHAT CUSTOMER SAYS</h2>
  <div class="rule" style="left:508px;top:3379px;width:194px;height:2px"></div>

  <div class="review review-side" style="left:159px;top:3467px;width:200px;height:193px;padding:48px 50px 0 20px">
    <p>Lorem ipsum dolor sit amet, sed do eiusmod tempor incididunt aliqua. Quis ipsum suspendisse modo viverra maecenas</p>
  </div>
  <div class="review review-side" style="left:850px;top:3467px;width:161px;height:193px;padding:48px 14px 0 40px;text-align:left">
    <p>adipiscing elit, sed dolore magna gravida. Risus commodo lacus vel</p>
    <div style="position:absolute;right:22px;bottom:20px;width:14px;height:14px;border-radius:50%;background:#c8cdd0"></div>
  </div>
  <div class="review" style="left:326px;top:3426px;width:554px;height:269px;padding:0 50px">
    <svg style="position:absolute;left:254px;top:30px" width="46" height="34" viewBox="0 0 46 34"><path fill="#1d6c84" d="M4 34V18C4 8 10 2 19 0l2 5c-6 2-9 6-9 11h8v18zM28 34V18c0-10 6-16 15-18l2 5c-6 2-9 6-9 11h8v18z"/></svg>
    <p style="margin-top:72px">Lorem ipsum dolor sit amet, consectetur adipiscing elit, sed do eiusmod tempor incididunt ut labore et dolore magna aliqua. Quis ipsum suspendisse ultrices gravida. Risus commodo viverra maecenas accumsan lacus vel</p>
    <div style="margin-top:12px;font-size:14.5px;font-weight:700;color:var(--ink)">Daniel Hartwell</div>
    <div style="font-size:19px;color:var(--orange);letter-spacing:2px;line-height:22px">★★★★★</div>
    <div style="position:absolute;right:30px;bottom:26px;width:20px;height:20px;border-radius:50%;background:#c8cdd0"></div>
  </div>
  <div class="abs icon-circle" style="left:555px;top:3720px;width:42px;height:42px;background:var(--teal)"><svg width="18" height="14" viewBox="0 0 18 14"><path d="M17 7H2M7 1L1 7l6 6" fill="none" stroke="#fff" stroke-width="2"/></svg></div>
  <div class="abs icon-circle" style="left:609px;top:3720px;width:42px;height:42px;background:var(--teal)"><svg width="18" height="14" viewBox="0 0 18 14"><path d="M1 7h15M11 1l6 6-6 6" fill="none" stroke="#fff" stroke-width="2"/></svg></div>

  <!-- CONTACT -->
  <section class="abs contact-left" role="img" aria-label="Dark commercial kitchen background"></section>
  <section class="abs contact-right"></section>

  <div class="abs" style="left:150px;top:3953px;font-size:16px;color:var(--white)">GET IN TOUCH</div>
  <h2 class="abs" style="left:148px;top:3975px;font-size:40px;font-weight:700;color:var(--white)">CONTACT US</h2>
  <p class="abs" style="left:153px;top:4060px;width:410px;font-size:15px;line-height:23px;color:var(--white)">Call, Text or Email to book a consultation and get your free energy saving report.</p>
  <div class="contact-item" style="top:4136px">
    <div class="ic"><svg width="18" height="22" viewBox="0 0 18 22"><path fill="#26292b" d="M9 0a8 8 0 0 0-8 8c0 6 8 14 8 14s8-8 8-14a8 8 0 0 0-8-8zm0 11a3 3 0 1 1 0-6 3 3 0 0 1 0 6z"/></svg></div>
    <div>2480 Harbor Crest Blvd.,<br>Bayview, FL 33099</div>
  </div>
  <div class="contact-item" style="top:4206px">
    <div class="ic"><svg width="18" height="18" viewBox="0 0 24 24"><path fill="#26292b" d="M6.6 10.8a15 15 0 0 0 6.6 6.6l2.2-2.2c.3-.3.7-.4 1-.2 1.1.4 2.3.6 3.6.6.6 0 1 .4 1 1V20c0 .6-.4 1-1 1A17 17 0 0 1 3 4c0-.6.4-1 1-1h3.5c.6 0 1 .4 1 1 0 1.3.2 2.5.6 3.6.1.3 0 .7-.2 1z"/></svg></div>
    <div>Phone Number<br>+100 555 0142</div>
  </div>
  <div class="contact-item" style="top:4277px">
    <div class="ic"><svg width="20" height="15" viewBox="0 0 20 15"><rect x="1" y="1" width="18" height="13" fill="none" stroke="#26292b" stroke-width="2"/><path d="M1 1l9 7 9-7" fill="none" stroke="#26292b" stroke-width="2"/></svg></div>
    <div>Email address<br>info@meridiankitchen.example</div>
  </div>

  <h2 class="abs" style="left:685px;top:3940px;font-size:30px;font-weight:600;color:var(--white)">REQUEST&nbsp; A SERVICE</h2>
  <div class="field" style="left:685px;top:3998px;width:208px;height:43px">First Name</div>
  <div class="field" style="left:900px;top:3998px;width:222px;height:43px">Last Name</div>
  <div class="field" style="left:685px;top:4056px;width:437px;height:43px">Email address</div>
  <div class="field" style="left:685px;top:4111px;width:437px;height:43px">Phone Number</div>
  <div class="field" style="left:685px;top:4163px;width:437px;height:84px">Leave Message</div>
  <div class="btn btn-orange" style="left:685px;top:4267px;width:200px;height:48px;font-size:14px">SEND MESSAGE ›</div>

  <!-- FOOTER -->
  <svg class="abs" style="left:0;top:4400px" width="1200" height="369" viewBox="0 0 1200 369">
    <polygon points="0,82 593,17 1200,54 1200,369 0,369" fill="#fff"/>
  </svg>
  <div class="abs" style="left:573px;top:4440px;width:40px;height:40px;border:4px solid var(--teal)"></div>
  <div class="abs" style="left:493px;top:4510px;width:200px;text-align:center;font-size:20px;font-weight:700;color:var(--teal)">MERIDIAN</div>
  <div class="abs" style="left:493px;top:4535px;width:200px;text-align:center;font-size:8.5px;font-weight:700;letter-spacing:2px;color:var(--teal)">RESTAURANT SERVICE</div>

  <nav class="footer-nav">
    <a style="left:131px">HOME</a>
    <span class="footer-dot" style="left:199px"></span>
    <a style="left:226px">ABOUT US</a>
    <span class="footer-dot" style="left:322px"></span>
    <a style="left:354px">SERVICES</a>
    <a style="left:726px">WHY US</a>
    <span class="footer-dot" style="left:805px"></span>
    <a style="left:837px">REVIEWS</a>
    <span class="footer-dot" style="left:929px"></span>
    <a style="left:957px">CONTACT US</a>
  </nav>
  <div class="abs" style="left:115px;top:4574px;width:952px;height:1px;background:#d8dcdf"></div>
  <div class="footer-contact" style="left:132px">
    <div class="icon-circle" style="width:40px;height:40px;background:var(--teal)"><svg width="16" height="20" viewBox="0 0 18 22"><path fill="#fff" d="M9 0a8 8 0 0 0-8 8c0 6 8 14 8 14s8-8 8-14a8 8 0 0 0-8-8zm0 11a3 3 0 1 1 0-6 3 3 0 0 1 0 6z"/></svg></div>
    2480 Harbor Crest Blvd., Bayview, FL 33099
  </div>
  <div class="footer-contact" style="left:563px">
    <div class="icon-circle" style="width:40px;height:40px;background:var(--teal)"><svg width="16" height="16" viewBox="0 0 24 24"><path fill="#fff" d="M6.6 10.8a15 15 0 0 0 6.6 6.6l2.2-2.2c.3-.3.7-.4 1-.2 1.1.4 2.3.6 3.6.6.6 0 1 .4 1 1V20c0 .6-.4 1-1 1A17 17 0 0 1 3 4c0-.6.4-1 1-1h3.5c.6 0 1 .4 1 1 0 1.3.2 2.5.6 3.6.1.3 0 .7-.2 1z"/></svg></div>
    +1 555-014-2298
  </div>
  <div class="footer-contact" style="left:786px">
    <div class="icon-circle" style="width:40px;height:40px;background:var(--teal)"><svg width="18" height="13" viewBox="0 0 20 15"><rect x="1" y="1" width="18" height="13" fill="none" stroke="#fff" stroke-width="2"/><path d="M1 1l9 7 9-7" fill="none" stroke="#fff" stroke-width="2"/></svg></div>
    enquiry@meridiankitchen.example
  </div>
  <div class="abs" style="left:115px;top:4680px;width:952px;height:1px;background:#d8dcdf"></div>
  <div class="abs" style="left:131px;top:4715px;font-size:13.5px;color:var(--text)">Copyright © 2025 Meridian. All Right Reserved</div>
  <span class="social" style="left:978px"></span>
  <span class="social" style="left:1014px"></span>
  <span class="social" style="left:1051px"></span>
  <svg class="abs" style="left:1120px;top:4706px" width="16" height="22" viewBox="0 0 16 22"><path d="M8 21V2M2 8l6-6 6 6" fill="none" stroke="#222a2e" stroke-width="2"/></svg>

</div>
</body>
</html>
```